Parcelnook.com.au Front page Re-Design

We need a front page redesign for the website parcelnook.com.au,
The site needs to keep a number of products products highlighted on the front page. Same buttons but navigation could be different and we still need some text for SEO.
What we do not currently like:
1. The big banners.
2. The use of too much orange especially the 50% orange borders.
3. the fact that products cannot be seen straight away when logged-in.
4. The fact that it is hard to convert to tablet friendly
5. The fact that it's not a modern design.

What we think we want:

1. Maybe more use of 1 colour (purple or orange) with the other a secondary highlight colour.
2. A more modern look
3. The wow factor

Look at parcelnook.com.au take the elements that you need and design.
Updates

Project Deadline Extended
Reason: Designs are getting better. liking the designs that don't look like the usual e-commerce templates out there.

Hello,

We are making decisions next Monday. Sorry for the delay but there has been a lot of holidays in Australia and decision makers away.

Industry/Entity Type

Seo

Colors
6b449b
f78f20
ffffff

```html
<!DOCTYPE html>
<html lang="en">
<head>
<meta charset="utf-8">
<title>Parcelnook.com.au – Gift Hampers Australia Wide</title>
<link rel="stylesheet" href="https://fonts.googleapis.com/css2?family=Open+Sans:wght@300;400;600;700&display=swap">
<style>
:root{
  --purple:#6b449b;
  --purple-deep:#5a3686;
  --orange:#f78f20;
  --white:#ffffff;
  --page:#f3f3f3;
  --panel:#e9e9e9;
  --line:#d6d6d6;
  --text:#4a4a4a;
  --muted:#8a8a8a;
}
*{box-sizing:border-box;margin:0;padding:0}
html,body{width:742px;height:1200px;overflow:hidden}
body{position:relative;background:var(--page);font-family:"Open Sans",Arial,sans-serif;color:var(--text)}
a{color:inherit;text-decoration:none}
ul{list-style:none}
.abs{position:absolute}

/* header */
.brand{left:100px;top:8px;width:130px}
.brand-name{display:flex;align-items:center;gap:5px;font-size:15px;font-weight:700;color:var(--purple);line-height:1}
.brand-mark{width:14px;height:14px;background:var(--orange);flex:none}
.brand-tag{margin-top:6px;font-size:7.5px;font-weight:600;color:var(--purple)}
.welcome{left:259px;top:12px;font-size:9px;font-weight:700;color:#333}
.account-tab{left:462px;top:0;width:180px;height:18px;background:var(--purple);border-radius:0 0 0 12px;display:flex;justify-content:space-around;align-items:center;padding-left:10px;font-size:7.5px;color:var(--white)}
.account-tab span.sep{opacity:.6}
.search{left:259px;top:33px;width:197px;height:21px;background:#eaeaea;border:1px solid var(--line);display:flex;align-items:center;justify-content:space-between;padding:0 8px;font-size:7.5px;color:var(--muted)}
.quick-links{left:484px;top:37px;font-size:8.5px;color:var(--orange)}
.quick-links .sep{color:var(--muted);margin:0 6px}
.cart{left:582px;top:33px;width:60px;height:21px;background:#eaeaea;border:1px solid var(--line);display:flex;align-items:center;justify-content:center;gap:6px;font-size:8px;color:var(--orange)}

.main-nav{left:100px;top:66px;width:542px;height:21px;background:var(--purple);display:flex;font-size:8.5px;color:var(--white)}
.main-nav li{flex:auto;display:flex;align-items:center;justify-content:center}
.main-nav li.active{background:var(--orange);flex:0 0 41px}

.info-bar{left:100px;top:94px;width:542px;height:26px;background:var(--white);border:1px solid var(--line);display:flex;font-size:8px;color:#555}
.info-bar li{flex:1;display:flex;align-items:center;justify-content:center;gap:8px}
.info-bar li+li{border-left:1px solid var(--line)}
.price-badge{width:30px;height:20px;border-radius:50%;background:#e4e4e4;border:1px solid #c9c9c9}

/* sidebar */
.side-box{left:100px;width:140px;background:var(--panel);box-shadow:0 2px 0 #d9d9d9;padding-bottom:8px}
.side-box h3{padding:13px 12px 8px;font-weight:400;color:var(--purple);line-height:1.1}
.side-box h3 small{display:block;font-size:8.5px}
.side-box h3 span{font-size:13.5px;text-transform:uppercase}
.side-box li{height:18px;margin:0 6px 0 0;padding-left:12px;display:flex;align-items:center;gap:6px;font-size:7.5px;color:#666;border-bottom:1px dotted #c8c8c8}
.side-box li::before{content:"";width:3px;height:3px;background:var(--orange)}
.side-box li.active{background:var(--purple);color:var(--white);border-bottom:none;margin-right:6px}
.box-price{top:128px;height:161px}
.box-style{top:308px;height:222px}
.box-occasion{top:554px;height:143px}

.flowers{left:100px;top:714px;width:140px;height:142px;background:radial-gradient(circle at 50% 65%,#f5a43a 0%,#e0622a 35%,#9c1c1c 75%,#4a0c0c 100%)}
.flowers p{padding-top:20px;text-align:center;font-size:9px;font-weight:700;color:var(--white)}

.seo-box{left:100px;top:870px;width:140px;height:148px;background:var(--orange);padding:12px 10px;text-align:center;color:var(--white)}
.seo-box h4{font-size:14px;font-weight:400;color:var(--purple);margin-bottom:5px}
.seo-box p{font-size:6.6px;line-height:1.55}

/* hero slider */
.slider{left:251px;top:128px;width:391px;height:244px}
.slide{position:absolute;inset:0 0 20px 0;background:linear-gradient(100deg,#7a1d3a 0%,#b83a58 40%,#d8607b 70%,#c9324e 100%)}
.slide-copy{position:absolute;left:24px;top:12px;width:170px;color:var(--white)}
.slide-copy h2{font-size:17px;font-weight:400;line-height:1.2}
.slide-copy .lead{font-size:9.5px;line-height:1.2;margin:3px 0 7px}
.slide-copy .body{font-size:6.6px;line-height:1.4}
.buy-now{position:absolute;left:24px;top:158px;width:95px;height:20px;background:var(--orange);color:var(--white);font-size:9.5px;font-weight:600;display:flex;align-items:center;justify-content:center}
.slide-arrow{position:absolute;top:68px;width:16px;height:28px;background:var(--orange);display:flex;align-items:center;justify-content:center}
.slide-arrow.prev{left:0;border-radius:0 14px 14px 0}
.slide-arrow.next{right:0;border-radius:14px 0 0 14px}
.slider-strip{position:absolute;left:0;bottom:0;width:100%;height:20px;background:var(--purple);display:flex;justify-content:center;align-items:center;gap:4px}
.slider-strip i{width:4px;height:4px;border-radius:50%;background:#c9b7de}
.slider-strip i.on{background:var(--white)}

/* intro */
.intro{left:251px;top:388px;width:391px}
.intro h1{font-size:13px;font-weight:400;color:var(--orange);line-height:1.3;text-transform:uppercase}
.intro p{margin-top:6px;font-size:8.4px;line-height:1.45;color:#555}
.section-title{left:251px;top:488px;font-size:14px;font-weight:400;color:var(--orange);text-transform:uppercase}

/* products */
.product{width:122px;height:162px;background:var(--panel);border-bottom:2px solid var(--orange);padding:7px 7px 0;text-align:center;overflow:hidden}
.product .photo{height:112px;background:radial-gradient(circle at 50% 55%,#b89a7a 0%,#e9e2da 55%,#ffffff 80%);border:1px solid #e0e0e0}
.product h5{margin-top:8px;font-size:7px;font-weight:600;color:var(--purple)}
.product .price{margin-top:3px;font-size:9px;font-weight:700;color:var(--orange)}
.ribbon{position:absolute;left:0;top:0;width:0;height:0;border-top:30px solid var(--purple);border-right:30px solid transparent}
.ribbon-text{position:absolute;left:2px;top:7px;font-size:6.5px;color:var(--white);transform:rotate(-45deg)}
.product-actions{left:413px;top:676px;display:flex;gap:4px}
.product-actions span{width:16px;height:12px;background:#e1e1e1;display:flex;align-items:center;justify-content:center}
.product-actions span.cart-btn{background:var(--purple)}

/* footer */
.footer{left:100px;top:1092px;width:542px;height:108px;background:var(--purple);color:var(--white)}
.footer-links{position:absolute;top:23px;font-size:6.4px;line-height:11px;text-transform:uppercase}
.footer-links li::before{content:"\2022";margin-right:6px;color:#c9b7de}
.payments{position:absolute;left:298px;top:34px;display:flex;gap:3px}
.payments span{width:14px;height:10px;background:#e9e3f2;border-radius:1px}
.payments span.round{width:10px;border-radius:50%}
.connect{position:absolute;left:14px;top:88px;display:flex;align-items:center;gap:3px;font-size:9px;font-weight:700}
.connect b{margin-right:5px}
.connect span{width:10px;height:10px;background:#c9b7de}
.copyright{position:absolute;left:305px;top:93px;font-size:5.6px;color:#ddd}
.signup{position:absolute;right:0;top:0;width:136px;height:108px;background:var(--orange);padding:13px 12px}
.signup h4{font-size:12px;font-weight:400;border-bottom:1px solid rgba(255,255,255,.4);padding-bottom:6px}
.signup p{margin-top:8px;font-size:6.2px;line-height:1.45}
.signup-field{margin-top:10px;height:18px;background:var(--white);display:flex;align-items:center;justify-content:space-between;padding:0 6px;font-size:6.4px;color:var(--muted)}
</style>
</head>
<body>

<!-- Header -->
<div class="abs brand">
  <div class="brand-name"><span class="brand-mark"></span>parcelnook.com.au</div>
  <div class="brand-tag">parcel &amp; hamper network</div>
</div>
<div class="abs welcome">Hi ! &nbsp;Welcome to parcelnook</div>
<nav class="abs account-tab"><a>Login</a><span class="sep">|</span><a>Register</a><span class="sep">|</span><a>Help</a><span class="sep">|</span><a>Store finder</a></nav>
<div class="abs search"><span>Search gifts</span>
  <svg width="9" height="9" viewBox="0 0 10 10"><circle cx="4" cy="4" r="3" fill="none" stroke="#777" stroke-width="1.2"/><line x1="6.3" y1="6.3" x2="9.3" y2="9.3" stroke="#777" stroke-width="1.2"/></svg>
</div>
<div class="abs quick-links"><a>Wish list</a><span class="sep">|</span><a>Checkout</a></div>
<div class="abs cart">
  <svg width="13" height="11" viewBox="0 0 13 11"><path d="M0 1h2.5l1.8 6h6.5l1.5-4.5H3.4" fill="none" stroke="#f78f20" stroke-width="1.3"/><circle cx="5" cy="9.5" r="1.1" fill="#f78f20"/><circle cx="10" cy="9.5" r="1.1" fill="#f78f20"/></svg>
  <span>0 items</span>
</div>

<ul class="abs main-nav">
  <li class="active">Easter</li><li>Mothers Day</li><li>Get Well</li><li>Thank you</li><li>Birthday</li><li>Anniversary</li><li>Romance</li><li>New Baby</li><li>Childrens</li><li>For Him</li><li>For Her</li>
</ul>

<ul class="abs info-bar">
  <li><svg width="14" height="14" viewBox="0 0 14 14"><circle cx="7" cy="7" r="6.3" fill="none" stroke="#999"/><path d="M5 4l1 1.8-.7.9c.5 1 1.2 1.7 2.2 2.2l.9-.7L10 9.2 9.3 10.3C7 10 4.2 7.3 3.8 5z" fill="#999"/></svg>+61 1300 555 018</li>
  <li><span class="price-badge"></span>Lowest Price Guarantee</li>
  <li><svg width="14" height="10" viewBox="0 0 14 10"><rect x=".5" y=".5" width="13" height="9" fill="none" stroke="#999"/><path d="M.5.5L7 5.5 13.5.5" fill="none" stroke="#999"/></svg>Subscribe to our Newsletter</li>
</ul>

<!-- Sidebar -->
<aside class="abs side-box box-price">
  <h3><small>Shop by</small><span>Basket Price</span></h3>
  <ul><li class="active">Gifts under $50</li><li>Gifts $50 to $75</li><li>Gifts $50 to $75</li><li>Gifts $75 to $100</li><li>Gifts $100 to $150</li><li>Gifts Over $150</li></ul>
</aside>
<aside class="abs side-box box-style">
  <h3><small>Shop by</small><span>Basket Style</span></h3>
  <ul><li class="active">Chocolate Bouquets</li><li>Plant Gifts</li><li>Fruit Hampers</li><li>Pamper Packs</li><li>Lollies &amp; Sweets</li><li>Teddy Bears &amp; Toys</li><li>Gourmet Hampers</li><li>Champagne &amp; Liquor</li><li>Personalised Items</li><li>Corporate Items</li></ul>
</aside>
<aside class="abs side-box box-occasion">
  <h3><small>Shop by</small><span>Occasions</span></h3>
  <ul><li class="active">Easter Gifts</li><li>Mothers Day Gifts</li><li>Fathers Day Gifts</li><li>Christmas Gifts</li><li>Valentines Day Gifts</li></ul>
</aside>
<div class="abs flowers" role="img" aria-label="Bouquet of orange and red roses"><p>Bouquets of FLOWERS</p></div>
<div class="abs seo-box">
  <h4>SEO</h4>
  <p>Lorem Ipsum is simply dummy text of the printing and typesetting industry. Lorem Ipsum has been the industry's standard dummy text ever since the 1500s, when an unknown printer took a galley of type and scrambled it to make a type specimen book. It has survived not only five centuries, but also the leap into electronic typesetting, remaining</p>
</div>

<!-- Hero slider -->
<section class="abs slider">
  <div class="slide" role="img" aria-label="Smiling woman holding a wrapped gift box beside a teddy bear"></div>
  <div class="slide-copy">
    <h2>Gourmet hampers</h2>
    <p class="lead">Gourmet hampers and delicious gourmet food baskets, for sale Australia wide!</p>
    <p class="body">All of our Gourmet hampers for sale are available to buy online 24 hours a day with optional extras like chocolates, teddies, balloons, cards and more. Gourmet gift Hampers &amp; Food baskets full of treats and delicious delicacies! Sweet, Sour, Salty or Savory we have somethings for every taste available, with delivery across Australia!</p>
  </div>
  <a class="buy-now">Buy Now!</a>
  <span class="slide-arrow prev"><svg width="6" height="8" viewBox="0 0 6 8"><path d="M5 0L0 4l5 4z" fill="#fff"/></svg></span>
  <span class="slide-arrow next"><svg width="6" height="8" viewBox="0 0 6 8"><path d="M1 0l5 4-5 4z" fill="#fff"/></svg></span>
  <div class="slider-strip"><i></i><i class="on"></i><i></i></div>
</section>

<!-- Intro -->
<section class="abs intro">
  <h1>Gourmet hampers for sale online with delivery<br>Australia wide !</h1>
  <p>Next Day Delivery Avilable When ordered by 2pm EDST Weekdays.<br>Simply place your order online or over the phone on 1300 555 018.<br>Excludes areas throught rural and outback Australia where an additional 2 days may be Required.<br>Our Store Business Hours : 09:00 AM - 05:00 PM, EDST.</p>
</section>
<h2 class="abs section-title">Gift Hampers</h2>

<!-- Products -->
<article class="abs product" style="left:251px;top:518px"><span class="ribbon"></span><span class="ribbon-text">New</span><div class="photo" role="img" aria-label="Gift chest with wine, cheese and crackers"></div><h5>Chalk and Chess Gift Chest</h5><p class="price">$89.95</p></article>
<article class="abs product" style="left:385px;top:518px;height:156px"><span class="ribbon"></span><span class="ribbon-text">New</span><div class="photo" role="img" aria-label="Gift chest filled with sweets and snacks"></div><h5>Sweet Delicious Gift Chest</h5><p class="price">$99.95</p></article>
<div class="abs product-actions">
  <span class="cart-btn"><svg width="9" height="8" viewBox="0 0 13 11"><path d="M0 1h2.5l1.8 6h6.5l1.5-4.5H3.4" fill="none" stroke="#f78f20" stroke-width="1.6"/><circle cx="5" cy="9.5" r="1.2" fill="#f78f20"/><circle cx="10" cy="9.5" r="1.2" fill="#f78f20"/></svg></span>
  <span><svg width="7" height="7" viewBox="0 0 8 8"><rect x="0.5" y="2" width="5" height="5.5" fill="none" stroke="#555"/><rect x="2.5" y="0.5" width="5" height="5.5" fill="#e1e1e1" stroke="#555"/></svg></span>
  <span><svg width="7" height="7" viewBox="0 0 10 9"><path d="M5 8.5L1 4.5C-.5 3 .5 0 3 .8 4 1.1 5 2.5 5 2.5S6 1.1 7 .8C9.5 0 10.5 3 9 4.5z" fill="#555"/></svg></span>
</div>
<article class="abs product" style="left:520px;top:518px"><span class="ribbon"></span><span class="ribbon-text">New</span><div class="photo" role="img" aria-label="Potted thyme with kitchen condiments on a board"></div><h5>Natural Thyme Kitchen Gift Set</h5><p class="price">$89.95</p></article>

<article class="abs product" style="left:251px;top:708px"><span class="ribbon"></span><span class="ribbon-text">New</span><div class="photo" role="img" aria-label="Potted rosemary with oils and spices"></div><h5>Natural Rosemary Kitchen Gift Set</h5><p class="price">$99.95</p></article>
<article class="abs product" style="left:385px;top:708px"><span class="ribbon"></span><span class="ribbon-text">New</span><div class="photo" role="img" aria-label="Wooden crate of gourmet foods on wood shavings"></div><h5>Natural Rosemary Kitchen Gift Set</h5><p class="price">$99.95</p></article>
<article class="abs product" style="left:520px;top:708px"><span class="ribbon"></span><span class="ribbon-text">New</span><div class="photo" role="img" aria-label="Picnic platter board with crackers and preserves"></div><h5>Picnic Platter Gift Pack</h5><p class="price">$129.95</p></article>

<article class="abs product" style="left:251px;top:898px"><span class="ribbon"></span><span class="ribbon-text">New</span><div class="photo" role="img" aria-label="Barbecue gift basket with sauces and an apron"></div><h5>Backyard Barbecue Gift Basket</h5><p class="price">$149.95</p></article>
<article class="abs product" style="left:385px;top:898px"><span class="ribbon"></span><span class="ribbon-text">New</span><div class="photo" role="img" aria-label="Wooden tray hamper of sweet treats"></div><h5>Sweet Things Gourmet Hamper</h5><p class="price">$47.50</p></article>
<article class="abs product" style="left:520px;top:898px"><span class="ribbon"></span><span class="ribbon-text">New</span><div class="photo" role="img" aria-label="Potted oregano with kitchen condiments on a board"></div><h5>Natural Oregano Kitchen Gift Set</h5><p class="price">$99.95</p></article>

<!-- Footer -->
<footer class="abs footer">
  <ul class="footer-links" style="left:15px"><li>Easter</li><li>Mothers Day</li><li>Get Well</li><li>Thank You</li><li>Birthday</li></ul>
  <ul class="footer-links" style="left:115px"><li>Anniversary</li><li>Romance</li><li>New Baby</li><li>Childrens</li><li>For Him</li></ul>
  <ul class="footer-links" style="left:218px"><li>Price</li><li>Style</li><li>Occasions</li></ul>
  <div class="payments"><span></span><span></span><span></span><span></span><span class="round"></span></div>
  <div class="connect"><b>CONNECT WITH US</b><span></span><span></span><span></span><span></span><span></span><span></span></div>
  <p class="copyright">© Copyright 2014. All Rights Reserved</p>
  <div class="signup">
    <h4>SIGN UP</h4>
    <p>Lorem Ipsum is simply dummy text of the printing and typesetting industry.</p>
    <div class="signup-field"><span>Email Address</span><svg width="9" height="8" viewBox="0 0 10 9"><path d="M0 0l10 4.5L0 9l1.5-4.5z" fill="#333"/></svg></div>
  </div>
</footer>

</body>
</html>
```